Logo für Trockenbauarbeiten aller Art, Spachtelarbeiten und Verputzarbeiten
Zielgruppe
Gegenstand des Unternehmens ist Trockenbauarbeiten aller Art, Spachtelarbeiten und Verputzarbeiten.
Unsere Zielgruppe sind Menschen ab 30 Jahren aufwärts, wir interessieren uns für den einzelnen Hausbesitzer oder Eigentumswohnungbesitzer. Wir benötigen einen hohen Wiedererkennungseffekt.
Wir benötigen Designvorlagen für eine Facebook Seite, Instagram und werden über diese beiden Plattformen auch Werbung schalten, daher benötigen wir dafür auch die verschiedenen Designvorlagen, um verschiedenen Werbekampangen zu erstellen.
Name des Unternehmens: 'WAND-PLAN KOLLHAGEN GmbH'
Aufgabenstellung
Wichtig ist bei den verschiedenen Designs, dass wir Leads bzw. Kundenaufträge sammeln können. Wir müssen herausstechen aus der Masse an Handwerkern. Wir sind die absoluten Spezialisten in unserem Gebiet. Des Weiteren werden wir aus den Materialen diverse Kampagnen erstellen die das komplette Jahr 2022 durchlaufen werden. Vorzugsweise werden wir hierfür die Plattfirm Facebook verwenden, aber auch andere Kanäle.
WICHTIG: Das Logo mit dem roten Haus ist unser original Logo!

```html
<!DOCTYPE html>
<html lang="de">
<head>
<meta charset="utf-8">
<title>WAND-PLAN KOLLHAGEN – Social Post</title>
<link href="https://fonts.googleapis.com/css2?family=Montserrat:wght@800&family=Open+Sans:wght@400;700&display=swap" rel="stylesheet">
<style>
  :root {
    --red: #ff0000;
    --red-bg: #ec1516;
    --dark: #383433;
    --white: #ffffff;
    --photo-light: #e9e8e6;
    --photo-mid: #b9a894;
    --photo-dark: #6f5b45;
  }
  html, body {
    margin: 0;
    padding: 0;
    width: 1200px;
    height: 1200px;
    overflow: hidden;
  }
  .canvas {
    position: relative;
    width: 1200px;
    height: 1200px;
    background: var(--red-bg);
  }
  .backdrop { position: absolute; inset: 0; }
  .post {
    position: absolute;
    left: 104px;
    top: 104px;
    width: 992px;
    height: 992px;
    background: var(--dark);
    box-shadow: 0 0 40px rgba(0,0,0,0.35);
    overflow: hidden;
  }
  .post-shapes { position: absolute; inset: 0; }
  .brand {
    position: absolute;
    left: 100px;
    top: 88px;
    color: var(--dark);
    font-family: "Montserrat", sans-serif;
    font-weight: 800;
    line-height: 1;
  }
  .brand-name { display: block; font-size: 42px; letter-spacing: 0.5px; }
  .brand-sub { display: block; font-size: 21px; margin-top: 8px; margin-left: 88px; letter-spacing: 1.5px; }
  .headline {
    position: absolute;
    left: 69px;
    top: 244px;
    margin: 0;
    color: var(--white);
    font-family: "Montserrat", sans-serif;
    font-weight: 800;
    font-size: 61px;
    line-height: 75px;
  }
  .headline-rule {
    position: absolute;
    left: 69px;
    top: 502px;
    width: 133px;
    height: 6px;
    background: var(--white);
  }
  .intro {
    position: absolute;
    left: 69px;
    top: 549px;
    width: 420px;
    margin: 0;
    color: var(--white);
    font-family: "Open Sans", sans-serif;
    font-size: 23.5px;
    line-height: 36.5px;
  }
  .about-title {
    position: absolute;
    left: 69px;
    top: 718px;
    margin: 0;
    color: var(--white);
    font-family: "Montserrat", sans-serif;
    font-weight: 800;
    font-size: 45px;
    line-height: 50px;
  }
  .about-text {
    position: absolute;
    left: 69px;
    top: 772px;
    width: 420px;
    margin: 0;
    color: var(--white);
    font-family: "Open Sans", sans-serif;
    font-size: 19.5px;
    line-height: 30.3px;
  }
  .phone {
    position: absolute;
    left: 600px;
    top: 830px;
    height: 62px;
    display: flex;
    align-items: center;
    gap: 20px;
    color: var(--white);
    font-family: "Open Sans", sans-serif;
    font-weight: 700;
    font-size: 38px;
  }
  .phone-icon { width: 50px; height: 50px; }
  .social {
    position: absolute;
    left: 589px;
    top: 932px;
    height: 36px;
    display: flex;
    align-items: center;
    gap: 14px;
    color: var(--white);
    font-family: "Open Sans", sans-serif;
    font-weight: 700;
    font-size: 22px;
  }
  .social-dot {
    width: 36px;
    height: 36px;
    border-radius: 50%;
    background: var(--white);
  }
</style>
</head>
<body>
<div class="canvas">
  <svg class="backdrop" width="1200" height="1200" viewBox="0 0 1200 1200">
    <polygon points="0,692 1200,524 1200,1200 0,1200" fill="var(--dark)"/>
  </svg>

  <div class="post">
    <svg class="post-shapes" width="992" height="992" viewBox="0 0 992 992">
      <polygon class="logo-panel" points="0,0 517,0 476,204 0,204" fill="var(--white)"/>
      <polygon class="accent-block" points="553,75 901,75 901,130 522,248" fill="var(--red)"/>
      <defs>
        <linearGradient id="photoTone" x1="0" y1="0" x2="1" y2="0">
          <stop offset="0" stop-color="var(--photo-dark)"/>
          <stop offset="0.4" stop-color="var(--photo-mid)"/>
          <stop offset="0.7" stop-color="var(--photo-light)"/>
          <stop offset="1" stop-color="var(--photo-light)"/>
        </linearGradient>
      </defs>
      <polygon class="photo" role="img" aria-label="Foto: Trockenbauer auf einer Leiter montiert Dämmung und Gipskartonplatten an einer Ständerwand" points="593,117 992,117 992,795 507,795 492,696" fill="url(#photoTone)"/>
      <polygon class="red-band" points="0,697 486,697 513,795 992,795 992,992 0,992" fill="var(--red)"/>
      <polygon class="phone-bar" points="514,828 992,828 992,894 527,894" fill="var(--dark)"/>
      <polygon class="footer-corner" points="0,918 364,918 350,992 0,992" fill="var(--dark)"/>
      <rect class="footer-line" x="0" y="950" width="558" height="2.5" fill="var(--white)"/>
    </svg>

    <div class="brand">
      <span class="brand-name">WAND-PLAN</span>
      <span class="brand-sub">KOLLHAGEN</span>
    </div>

    <h1 class="headline">Lorem<br>Ipsum dolor<br>sit amet</h1>
    <div class="headline-rule"></div>
    <p class="intro">consectetur adipiscing elit, sed do eiusmod tempor incididunt ut labore et dolore magna aliqua.</p>

    <h2 class="about-title">About us</h2>
    <p class="about-text">Lorem ipsum dolor sit amet, consectetur adipiscing elit, sed do eiusmod tempor incididunt ut labore et dolore magna aliqua. Ut enim ad minim veniam,</p>

    <div class="phone">
      <svg class="phone-icon" viewBox="0 0 50 50" aria-hidden="true">
        <path d="M10 6 C6 8 4 12 5 17 C7 27 16 39 27 45 C31 47 35 46 38 43 L40 41 L32 33 L28 36 C23 33 18 27 16 22 L20 18 L13 8 Z" fill="var(--white)"/>
        <path d="M28 10 A12 12 0 0 1 40 22" stroke="var(--white)" stroke-width="2.5" fill="none"/>
        <path d="M30 4 A18 18 0 0 1 46 20" stroke="var(--white)" stroke-width="2.5" fill="none"/>
      </svg>
      <span class="phone-number">0171/4829315</span>
    </div>

    <div class="social">
      <span class="social-dot"></span>
      <span class="social-handle">Wand_plan_kollhagen</span>
    </div>
  </div>
</div>
</body>
</html>
```